Sophrologist needs a cool signage at door entrance

I need signage for dr in sophrology based in Belgium (french speaking). The signed should capture the name the "Mireille Vantoorn" - "Naturopathe-Sophrologue-Reiki" and a catchphrase = (Healthy way of life)
« Fais du bien à ton corps, pour que ton âme ait envie d’y rester »
Requirements
Must have
- Hey,
Thats the instagram account for some inspiration www.instagram.com/mireille_serene_wellbeing
Light colors, green, blue
Healthy way of life
Size is 45cm wide on 30 cm high
The signage will be placed in front off woof pannel

```html
<!DOCTYPE html>
<html lang="fr">
<head>
<meta charset="utf-8">
<title>Mireille Vantoorn – Naturopathe-Sophrologue-Reiki</title>
<link rel="stylesheet" href="https://fonts.googleapis.com/css2?family=Lato:wght@700;900&display=swap">
<style>
  :root {
    --page: #e6e7e8;
    --sky-top: #1f5fb0;
    --sky-mid: #1aa3d8;
    --sea-light: #bfe6f4;
    --sand: #efe6cf;
    --sand-deep: #e2d4b2;
    --band: #0b6cb6;
    --band-text: #2a8ad0;
    --name: #ffffff;
    --motto: #1e4656;
    --stone: #e7e4dc;
  }
  html, body {
    margin: 0;
    width: 1200px;
    height: 869px;
    overflow: hidden;
    background: var(--page);
  }
  .sign {
    position: absolute;
    left: 15px;
    top: 44px;
    width: 1170px;
    height: 780px;
    display: block;
  }
  .sign-text { font-family: "Lato", Arial, sans-serif; }
  .name { fill: var(--name); font-weight: 900; font-size: 62px; }
  .profession { fill: var(--name); font-weight: 900; font-size: 60px; }
  .tagline { fill: var(--band-text); font-weight: 900; font-size: 160px; letter-spacing: 6px; }
  .motto { fill: var(--motto); font-weight: 900; font-size: 54px; }
</style>
</head>
<body>
<svg class="sign" viewBox="0 0 1245 830" xmlns="http://www.w3.org/2000/svg">
  <defs>
    <linearGradient id="beach" x1="0" y1="0" x2="0" y2="1">
      <stop offset="0" stop-color="var(--sky-top)"/>
      <stop offset="0.3" stop-color="var(--sky-mid)"/>
      <stop offset="0.72" stop-color="var(--sea-light)"/>
      <stop offset="0.82" stop-color="var(--sand)"/>
      <stop offset="1" stop-color="var(--sand-deep)"/>
    </linearGradient>
    <radialGradient id="stones" cx="0.5" cy="0.55" r="0.55">
      <stop offset="0" stop-color="var(--stone)"/>
      <stop offset="0.75" stop-color="var(--stone)" stop-opacity="0.7"/>
      <stop offset="1" stop-color="var(--stone)" stop-opacity="0"/>
    </radialGradient>
  </defs>

  <rect class="beach-scene" width="1245" height="830" fill="url(#beach)" role="img" aria-label="Illustration d'une plage ensoleillée avec mer et ciel bleu"/>

  <polygon class="band" points="0,307 1245,142 1245,437 0,602" fill="var(--band)"/>

  <g class="sign-text">
    <text class="tagline" transform="translate(75,440) rotate(-7.5)">HEALTHY WAY</text>
    <text class="tagline" transform="translate(347,522) rotate(-7.5)">OF LIFE</text>
  </g>

  <rect class="stones-shells" x="630" y="380" width="615" height="420" rx="120" fill="url(#stones)" role="img" aria-label="Illustration de galets empilés et de coquillages sur le sable"/>

  <g class="sign-text">
    <text class="name" transform="translate(47,190) rotate(-7.5)">Mireille Vantoorn</text>
    <text class="profession" transform="translate(62,275) rotate(-7.5)">Naturopathe-Sophrologue-Reiki</text>

    <text class="motto" transform="translate(65,655) rotate(-7.5)">Fais du bien à ton corps,</text>
    <text class="motto" transform="translate(72,720) rotate(-7.5)">pour que ton âme ait</text>
    <text class="motto" transform="translate(78,775) rotate(-7.5)">envie d’y rester</text>
  </g>
</svg>
</body>
</html>
```